Crestline Gas and Plumbing Business Card Design

I am after a business card design for my plumbing business called 'Crestline Gas & Plumbing'. I do all types of plumbing and gas work and specialise in general maintenance plumbing. Would like to see designs using current logo

Industry/Entity Type

Plumbing

Contact Information for Business Card

Name - Dale Whitcombe
Phone number - 0455163027
Email - admin@crestlinegasandplumbing.example.com.au
ABN - 68204915336

```html
<!DOCTYPE html>
<html lang="en">
<head>
<meta charset="utf-8">
<title>Crestline Gas &amp; Plumbing – Business Card</title>
<link rel="stylesheet" href="https://fonts.googleapis.com/css2?family=Exo+2:wght@400;800&family=Open+Sans:wght@400&display=swap">
<style>
  :root {
    --backdrop: #b5b6b9;
    --card: #000000;
    --blue-deep: #2e3192;
    --blue-mid: #1b75bc;
    --red: #e63a3a;
    --orange: #f7941d;
    --orange-text: #f7941d;
    --title-blue: #2b7ac9;
    --white: #ffffff;
  }
  html, body {
    margin: 0;
    padding: 0;
    width: 1200px;
    height: 1180px;
    overflow: hidden;
    background: var(--backdrop);
  }
  .canvas {
    position: relative;
    width: 1200px;
    height: 1180px;
  }
  .card {
    position: absolute;
    width: 835px;
    height: 477px;
    background: var(--card);
    border-radius: 36px;
    overflow: hidden;
  }
  .card--front { left: 311px; top: 71px; }
  .card--back  { left: 67px;  top: 610px; }

  .card__sweep {
    position: absolute;
    inset: 0;
    width: 100%;
    height: 100%;
  }

  .brand {
    position: absolute;
    display: flex;
    align-items: center;
    gap: 16px;
    font-family: "Exo 2", sans-serif;
    font-weight: 800;
    color: var(--title-blue);
    text-transform: uppercase;
    white-space: nowrap;
  }
  .brand__mark {
    flex: none;
    border-radius: 50%;
    background: var(--orange);
  }
  .brand--front { left: 46px; top: 120px; font-size: 30px; }
  .brand--front .brand__mark { width: 52px; height: 52px; }

  .brand--back {
    left: 0; right: 0; top: 190px;
    justify-content: center;
    font-size: 38px;
  }
  .brand--back .brand__mark { width: 64px; height: 64px; }

  .holder {
    position: absolute;
    left: 46px;
    top: 254px;
  }
  .holder__name {
    margin: 0;
    font-family: "Exo 2", sans-serif;
    font-weight: 800;
    font-size: 29px;
    letter-spacing: 0.5px;
    color: var(--orange-text);
    text-transform: uppercase;
    line-height: 1.1;
  }
  .holder__title {
    margin: 4px 0 0;
    font-family: "Exo 2", sans-serif;
    font-weight: 400;
    font-size: 25px;
    color: var(--title-blue);
    line-height: 1.1;
  }

  .contacts {
    position: absolute;
    right: 40px;
    top: 336px;
    margin: 0;
    padding: 0;
    list-style: none;
    font-family: "Open Sans", sans-serif;
    font-size: 19.5px;
    color: var(--white);
    text-align: right;
  }
  .contacts li {
    display: flex;
    justify-content: flex-end;
    align-items: center;
    gap: 12px;
    height: 37px;
  }
  .contacts svg { width: 19px; height: 19px; flex: none; }

  .website {
    position: absolute;
    left: 0; right: 0;
    top: 418px;
    text-align: center;
    font-family: "Open Sans", sans-serif;
    font-size: 20px;
    letter-spacing: 2.4px;
    color: var(--white);
  }
</style>
</head>
<body>
<div class="canvas">

  <section class="card card--front">
    <svg class="card__sweep" viewBox="0 0 800 457" preserveAspectRatio="none" aria-hidden="true">
      <defs>
        <linearGradient id="blueField" x1="0" y1="0" x2="1" y2="0">
          <stop offset="0" stop-color="var(--blue-deep)"/>
          <stop offset="0.55" stop-color="var(--blue-mid)"/>
          <stop offset="1" stop-color="var(--blue-deep)"/>
        </linearGradient>
        <linearGradient id="flameSwoosh" x1="0" y1="0" x2="1" y2="0">
          <stop offset="0" stop-color="var(--red)"/>
          <stop offset="0.45" stop-color="var(--orange)"/>
          <stop offset="0.8" stop-color="var(--orange)"/>
          <stop offset="1" stop-color="var(--red)"/>
        </linearGradient>
      </defs>
      <path d="M800,18 C700,150 600,285 430,355 C290,412 130,408 0,382 L0,457 L800,457 Z" fill="url(#blueField)"/>
      <path d="M0,334 C150,398 340,398 562,252 C380,372 170,408 0,374 Z" fill="url(#flameSwoosh)"/>
    </svg>

    <div class="brand brand--front">
      <span class="brand__mark"></span>
      <span class="brand__name">Crestline Gas &amp; Plumbing</span>
    </div>

    <div class="holder">
      <h1 class="holder__name">Dale Whitcombe</h1>
      <p class="holder__title">TITLE</p>
    </div>

    <ul class="contacts">
      <li>
        <span>0455163027</span>
        <svg viewBox="0 0 20 20" aria-hidden="true"><circle cx="10" cy="10" r="8.5" fill="none" stroke="#fff" stroke-width="1.6"/><path d="M7 5.5 L9 8 L8 9 C8.6 10.6 9.4 11.4 11 12 L12 11 L14.5 13 L13.3 14.6 C9.5 14.2 5.8 10.5 5.4 6.7 Z" fill="#fff"/></svg>
      </li>
      <li>
        <span>ABN - 68204915336</span>
        <svg viewBox="0 0 20 20" aria-hidden="true"><rect x="3" y="3" width="14" height="14" rx="2" fill="#fff"/><rect x="6" y="6" width="3" height="3" fill="#1b3f9c"/><rect x="11" y="6" width="3" height="3" fill="#1b3f9c"/><rect x="6" y="11" width="3" height="3" fill="#1b3f9c"/><rect x="11" y="11" width="3" height="3" fill="#1b3f9c"/></svg>
      </li>
      <li>
        <span>admin@crestlinegasandplumbing.example.com.au</span>
        <svg viewBox="0 0 20 20" aria-hidden="true"><path d="M2 8 L10 3 L18 8 L18 17 L2 17 Z" fill="#fff"/><path d="M2 8 L10 13 L18 8" fill="none" stroke="#2e3192" stroke-width="1.4"/></svg>
      </li>
    </ul>
  </section>

  <section class="card card--back">
    <div class="brand brand--back">
      <span class="brand__mark"></span>
      <span class="brand__name">Crestline Gas &amp; Plumbing</span>
    </div>
    <p class="website">www.crestlinegasandplumbing.example.com.au</p>
  </section>

</div>
</body>
</html>
```